Web Design Project - CCTV in Terravue Charts

I need a Design for a SAAS website.

The company is a B2B R&D company developing live CCTV video that's monitored on terravue charts & velmora globe.

We need a simple, calm & uncluttered design.
The site will be used for A/B testing of our products features.

The initial design will deal with the website.

Five Main Pages
Home
Products
DEMO - SAAS (selected designer to finalize)
Register
Generic Page

The generic page will be used for everything else, such as About us, Latest News, Contact us (same as register), support etc.

I have included a few mock ups just to give an idea of my initial thoughts on shapes, colours and simplicity of design, using Terravue Charts as a background. Each page or news article may have it's own geolocation, can this can be reflected in the design.

I would like this to all work in a Joomla type CMS so it can be easily updated and for A/B testing landing pages.(please advise me on the best system)

The second component to the website will be the SAAS administration area. We have the functional techie bit sorted but the design needs to fit branding.
This part of the project will be discussed with the designer upon selection of the most suitable design. We are hoping the designer will help with the look and feel of the administration section.

Many thanks for looking at this Project. Please contact me if if you need more information.

Logo & Logo Colour is indicatives only .

PS.
The following sites for their simplicity.
https://www.stashquill.com/home
I love the fact that its all about the product, not them.

http://www.valtremorides.com/en
This is the site that inspired the website idea.

It Company

• Terravue Chart Background
Greyed Out Terravue Chart background

```html
<!DOCTYPE html>
<html lang="en">
<head>
<meta charset="utf-8">
<title>Guarded Terra</title>
<link rel="stylesheet" href="https://fonts.googleapis.com/css2?family=PT+Sans:wght@400;700&family=PT+Sans+Narrow:wght@400&display=swap">
<style>
  :root {
    --brand-blue: #1e4f8c;
    --heading-blue: #1768a8;
    --slogan-blue: #3f6b9c;
    --text-grey: #4a4a4a;
    --nav-dark: #3c3c3c;
    --nav-light: #6e6e6e;
    --map-sea: #a9c0dd;
    --map-land: #eceae3;
    --footer-band: #a7bfe0;
    --footer-link: #1b3f7a;
    --button-top: #2a9ae0;
    --button-bottom: #0b66b5;
    --dot-idle: #a6bfdf;
    --dot-active: #f2a01c;
    --panel-white: #ffffff;
    --hairline: #dcdcdc;
  }
  * { box-sizing: border-box; margin: 0; padding: 0; }
  html, body { width: 1200px; height: 1068px; overflow: hidden; background: #fff; }
  body { position: relative; font-family: "PT Sans", sans-serif; color: var(--text-grey); }

  .site-header { position: absolute; left: 0; top: 0; width: 1200px; height: 88px; background: #fff; }
  .brand-name { position: absolute; left: 151px; top: 30px; font-family: "PT Sans", sans-serif; font-size: 26px; font-weight: 400; color: var(--brand-blue); }
  .main-nav { position: absolute; left: 508px; top: 33px; width: 521px; height: 32px; display: flex; border-radius: 3px; overflow: hidden;
    background: linear-gradient(to bottom, var(--nav-light), var(--nav-dark)); box-shadow: 0 1px 2px rgba(0,0,0,.4); }
  .main-nav a { flex: 1 1 auto; display: flex; align-items: center; justify-content: center; color: #fff; font-size: 12.5px; text-decoration: none; border-right: 1px solid #262626; }
  .main-nav a:last-child { border-right: none; }

  .map-band { position: absolute; left: 0; top: 88px; width: 1200px; height: 555px;
    background: linear-gradient(100deg, var(--map-land) 0%, var(--map-land) 22%, var(--map-sea) 32%, #c9d6e6 55%, var(--map-sea) 75%, #b5c9e2 100%); }

  .hero-panel { position: absolute; left: 224px; top: 165px; width: 769px; height: 367px; background: var(--panel-white); box-shadow: 0 3px 12px rgba(0,0,0,.35); }
  .hero-inner { position: absolute; left: 6px; top: 6px; right: 8px; bottom: 6px; border: 1px solid #e4e4e4; }
  .hero-slogan { position: absolute; left: 33px; top: 153px; font-family: "PT Sans Narrow", sans-serif; font-size: 31px; color: var(--slogan-blue); }
  .hero-globe { position: absolute; left: 398px; top: 0px; width: 356px; height: 356px; border-radius: 50%;
    background: radial-gradient(circle at 45% 40%, #ffffff 0%, #f3f4f6 70%, #e3e5e8 100%); border: 1px solid #b8b8b8; }
  .slide-dots { position: absolute; left: 37px; top: 300px; display: flex; gap: 5px; }
  .slide-dots span { width: 12px; height: 12px; border-radius: 50%; background: var(--dot-idle); }
  .slide-dots span.active { background: var(--dot-active); }

  .left-rule { position: absolute; left: 0; top: 643px; width: 1px; height: 338px; background: var(--hairline); }

  .features-panel { position: absolute; left: 142px; top: 578px; width: 930px; height: 300px; background: var(--panel-white); box-shadow: 0 2px 10px rgba(0,0,0,.3); }
  .feature { position: absolute; top: 22px; width: 290px; height: 172px; border-radius: 50%; border: 1px solid #ececec; text-align: center;
    background: radial-gradient(ellipse at center, #fff 60%, #f7f7f7 100%); }
  .feature h2 { margin-top: 24px; font-family: "PT Sans Narrow", sans-serif; font-weight: 400; font-size: 22px; color: var(--heading-blue); }
  .feature p { margin: 8px auto 0; width: 236px; font-size: 12.5px; line-height: 17px; color: var(--text-grey); }
  .feature p.narrow { width: 222px; }
  .learn-more { position: absolute; left: 50%; bottom: 21px; transform: translateX(-50%); width: 86px; height: 26px; border-radius: 3px;
    background: linear-gradient(to bottom, var(--button-top), var(--button-bottom)); color: #fff; font-size: 12px; line-height: 26px; text-decoration: none; box-shadow: 0 1px 2px rgba(0,0,0,.35); }

  .welcome-box { position: absolute; left: 160px; top: 787px; width: 892px; height: 205px; background: var(--panel-white); box-shadow: 0 1px 5px rgba(0,0,0,.3); }
  .welcome-box h1 { position: absolute; left: 13px; top: 14px; font-family: "PT Sans Narrow", sans-serif; font-weight: 400; font-size: 22px; color: var(--heading-blue); }
  .welcome-rule { position: absolute; left: 13px; right: 14px; top: 46px; height: 1px; background: #e5e5e5; }
  .welcome-box p { position: absolute; left: 19px; top: 60px; width: 570px; font-size: 11.4px; line-height: 24px; color: var(--text-grey); }
  .welcome-photo { position: absolute; left: 605px; top: 68px; width: 270px; height: 102px; border: 1px solid #9fb7d6;
    background: linear-gradient(90deg, #f2ead8 0%, #e9dcc4 40%, #d9c2a8 65%, #3a4250 100%); }

  .site-footer { position: absolute; left: 0; top: 981px; width: 1200px; height: 87px; background: var(--footer-band); text-align: center; }
  .footer-nav { margin-top: 31px; font-size: 12.5px; color: var(--footer-link); }
  .footer-nav a { color: var(--footer-link); text-decoration: none; }
  .footer-nav .sep { margin: 0 8px; }
  .copyright { margin-top: 6px; font-size: 12px; color: var(--footer-link); }
</style>
</head>
<body>
  <header class="site-header">
    <div class="brand-name">Guarded Terra</div>
    <nav class="main-nav">
      <a href="#" style="width:106px">Home</a>
      <a href="#" style="width:101px">Products</a>
      <a href="#" style="width:101px">Demo</a>
      <a href="#" style="width:103px">Register</a>
      <a href="#" style="width:110px">Contact Us</a>
    </nav>
  </header>

  <div class="map-band" role="img" aria-label="Greyed-out Terravue Charts world map background showing Europe, Africa and the Pacific"></div>

  <section class="hero-panel">
    <div class="hero-inner">
      <div class="hero-slogan">Connect with your assets online</div>
      <div class="hero-globe" role="img" aria-label="Line drawing of a globe showing Europe and Africa"></div>
      <div class="slide-dots"><span></span><span></span><span class="active"></span><span></span><span></span><span></span></div>
    </div>
  </section>

  <div class="left-rule"></div>

  <section class="features-panel">
    <article class="feature" style="left:16px">
      <h2>Create Global Assets</h2>
      <p>Create an online library of all your physical assets live video and status reports inside of velmora globe.</p>
      <a class="learn-more" href="#">Learn More &gt;&gt;</a>
    </article>
    <article class="feature" style="left:320px">
      <h2>Olympic Scalability</h2>
      <p class="narrow">Supporting 1000s of simulatiouns live video feeds and alarms guarded terra. starts small and scale to any size objet.</p>
      <a class="learn-more" href="#">Learn More &gt;&gt;</a>
    </article>
    <article class="feature" style="left:624px">
      <h2>Made to Touch</h2>
      <p>Guarded terra loves to be touched, it works on any devices either live or offline for when its really off the grid.</p>
      <a class="learn-more" href="#">Learn More &gt;&gt;</a>
    </article>
  </section>

  <section class="welcome-box">
    <h1>Welcome to our site</h1>
    <div class="welcome-rule"></div>
    <p>Lorem Ipsum is simply dummy text of the printing and typesetting industry. Lorem Ipsum has been the industry's standard dummy text ever since the 1500s, when an unknown printer took a galley of type and scrambled it to make a type specimen book. It has survived not only five centuries, but also the leap into electronic typesetting, remaining essentially unchanged. It was popularised in the 1960s with the release of Letraset sheets containing Lorem Ipsum passages, and more recently....</p>
    <div class="welcome-photo" role="img" aria-label="Photo of a business team in a bright office"></div>
  </section>

  <footer class="site-footer">
    <div class="footer-nav">
      <a href="#">Home</a><span class="sep">|</span><a href="#">Products</a><span class="sep">|</span><a href="#">DEMO</a><span class="sep">|</span><a href="#">Register</a><span class="sep">|</span><a href="#">Contact Us</a>
    </div>
    <div class="copyright">Copyrights @ 2012 All Rights Reserved</div>
  </footer>
</body>
</html>
```